Pitch Deck Foundation ÉlanJeu

ÉlanJeu is one of the largest non-profit organizations in Switzerland, which has been organizing free sports activities for children and young people for 25 years. We are active in the field of child and youth development in Switzerland and use sport as a means of addiction prevention, health promotion and social integration. With our programs, we open up vacant spaces for sports and encounters, creating the conditions for regular meeting places across cultural and social boundaries.

This presentation is to be given a new, modern design. It will be used when pitching to organizations with the goal of resulting in sponsoring partnerships and raising more donations

The pitch presentation should be structured in the following chapters: Intro (page 2-3), Facts and Figures (page 4-5), Topic Areas (page 6-14), Partnership Model (page 15-17), Closing (page 18-19).

Please make the colors and design according to the CI/CD, which was uploaded separately.

The goal is to arouse emotions with images.

Please make sure, that graphics display legibly.

Format 16:9

```html
<!DOCTYPE html>
<html lang="en">
<head>
<meta charset="utf-8">
<title>Pitch-Deck Foundation ÉlanJeu</title>
<link href="https://fonts.googleapis.com/css2?family=Inter:wght@600;700&family=Barlow:wght@400;500;600&family=Roboto+Condensed:wght@400&display=swap" rel="stylesheet">
<style>
  :root {
    --page: #cbe1eb;
    --brand: #00ade4;
    --brand-soft: #7fcbe8;
    --brand-mid: #2bb5e0;
    --dot-light: #1bb7ec;
    --dot-dark: #1a4fa8;
    --ink: #16191d;
    --grey-text: #5a5d61;
    --grey-small: #7a7d80;
    --panel-light: #f2f2f2;
    --panel-mid: #e8e8e8;
    --cover-bg: #dbeef6;
    --cover-bg-right: #c9ebf6;
    --white: #ffffff;
  }
  * { margin: 0; padding: 0; box-sizing: border-box; }
  html, body {
    width: 986px; height: 1200px; overflow: hidden;
    background: var(--page);
  }
  .canvas { position: relative; width: 986px; height: 1200px; }

  .slide {
    position: absolute; left: 133px; width: 720px; height: 405px;
    overflow: hidden;
    box-shadow: 20px 22px 34px rgba(70, 100, 120, 0.28);
  }
  .slide--cover { top: 137px; background: linear-gradient(90deg, var(--cover-bg) 0%, var(--cover-bg) 55%, var(--cover-bg-right) 100%); }
  .slide--problem { top: 633px; background: var(--panel-light); }

  .cover-graphic {
    position: absolute; left: 90px; top: 0; width: 630px; height: 405px;
    background: radial-gradient(ellipse 60% 70% at 70% 50%, rgba(43, 181, 224, 0.38) 0%, rgba(127, 203, 232, 0.18) 55%, rgba(219, 238, 246, 0) 100%);
  }

  .brand-mark {
    position: absolute; left: 25px; top: 19px;
    display: flex; align-items: center; gap: 6px;
    font-family: "Barlow", sans-serif; font-weight: 600;
    font-size: 15px; color: var(--brand); letter-spacing: 0.2px;
  }
  .brand-mark__square { width: 14px; height: 14px; background: var(--brand); }

  .dots { position: absolute; display: flex; gap: 9px; }
  .dots span { width: 5px; height: 5px; background: var(--dot-light); }
  .dots span:last-child { background: var(--dot-dark); width: 4px; height: 5px; }

  .cover-title {
    position: absolute; left: 42px; top: 163px;
    font-family: "Inter", sans-serif; font-weight: 700;
    font-size: 29px; line-height: 40px; color: var(--ink);
    letter-spacing: -0.2px;
  }

  .intro-panel { position: absolute; left: 0; top: 0; width: 270px; height: 100%; background: var(--panel-light); }
  .problem-title {
    position: absolute; left: 52px; top: 118px;
    font-family: "Inter", sans-serif; font-weight: 700;
    font-size: 21.5px; line-height: 27.5px; color: var(--ink);
  }
  .cta {
    position: absolute; left: 48px; top: 277px; width: 103px; height: 30px;
    background: var(--brand); color: var(--white);
    font-family: "Roboto Condensed", sans-serif; font-size: 10.5px;
    display: flex; align-items: center; justify-content: center; gap: 5px;
    box-shadow: 2px 3px 6px rgba(0,0,0,0.15);
  }
  .cta svg { width: 6px; height: 7px; }

  .entries { position: absolute; left: 270px; top: 0; width: 186px; height: 100%; background: var(--panel-mid); }
  .entry { position: absolute; left: 0; width: 186px; text-align: center; font-family: "Barlow", sans-serif; }
  .entry__icon { display: block; margin: 0 auto; width: 40px; height: 40px; }
  .entry__title { font-size: 10.5px; font-weight: 500; color: var(--grey-text); letter-spacing: 0.4px; margin-top: 12px; }
  .entry__text { font-size: 7px; line-height: 12.5px; color: var(--grey-small); letter-spacing: 0.3px; margin-top: 7px; }
  .entry--one { top: 29px; }
  .entry--three { top: 276px; }

  .entry-highlight {
    position: absolute; left: 251px; top: 155px; width: 218px; height: 95px;
    background: var(--brand); color: var(--white); text-align: center;
    font-family: "Barlow", sans-serif;
    box-shadow: 2px 3px 8px rgba(0,0,0,0.12);
  }
  .entry-highlight__title { font-size: 10.5px; font-weight: 600; letter-spacing: 0.4px; margin-top: 20px; }
  .entry-highlight__text { font-size: 7px; line-height: 12px; letter-spacing: 0.2px; margin: 8px 10px 0; }

  .photo {
    position: absolute; left: 456px; top: 0; width: 264px; height: 100%;
    background: linear-gradient(160deg, #0c0c0c 0%, #151311 45%, #4a4138 75%, #6d6458 100%);
  }
</style>
</head>
<body>
<main class="canvas">

  <section class="slide slide--cover">
    <div class="cover-graphic" role="img" aria-label="Decorative brand graphic in soft blue tones"></div>
    <div class="brand-mark"><span class="brand-mark__square"></span>ÉlanJeu</div>
    <div class="dots" style="left:43px; top:151px;"><span></span><span></span><span></span></div>
    <h1 class="cover-title">Pitch-Deck Foundation<br>ÉlanJeu</h1>
  </section>

  <section class="slide slide--problem">
    <div class="intro-panel"></div>
    <div class="brand-mark"><span class="brand-mark__square"></span>ÉlanJeu</div>
    <div class="dots" style="left:56px; top:104px;"><span></span><span></span><span></span></div>
    <h2 class="problem-title">More Difficult<br>Entry Into The<br>Labor Market<br>And The Adult<br>World</h2>
    <div class="cta">Get Your Style
      <svg viewBox="0 0 6 7"><path d="M0 0 L6 3.5 L0 7 Z" fill="currentColor"/></svg>
    </div>

    <div class="entries">
      <div class="entry entry--one">
        <svg class="entry__icon" viewBox="0 0 40 40" fill="none" stroke="var(--brand)" stroke-width="1.2" stroke-linecap="round">
          <path d="M20 11 a9 9 0 0 1 5.5 16 v4 h-11 v-4 A9 9 0 0 1 20 11 Z"/>
          <path d="M15 33.5 h10 M16 36 h8"/>
          <path d="M20 2 v4 M7 8 l3 3 M33 8 l-3 3 M3 20 h4 M33 20 h4 M7 32 l3 -3 M33 32 l-3 -3"/>
          <path d="M20 27 v-7 M17 20 h6"/>
        </svg>
        <p class="entry__title">Difficult Entry One</p>
        <p class="entry__text">The transition from school to vocational<br>education is complex and challenging.</p>
      </div>

      <div class="entry entry--three">
        <svg class="entry__icon" viewBox="0 0 40 40" fill="none" stroke="var(--brand)" stroke-width="1.2" stroke-linecap="round">
          <circle cx="20" cy="20" r="17"/>
          <path d="M20 29 C12 23 10 19 12 15.5 C14 12.5 18 13 20 16 C22 13 26 12.5 28 15.5 C30 19 28 23 20 29 Z"/>
        </svg>
        <p class="entry__title">Difficult Entry Three</p>
        <p class="entry__text">30 percent of 16- to 24-year-olds are<br>emotionally exhausted.</p>
      </div>
    </div>

    <div class="entry-highlight">
      <p class="entry-highlight__title">Difficult Entry Two</p>
      <p class="entry-highlight__text">The consequences: Orientation difficulties and excessive<br>demands; especially for young people from<br>disadvantaged families or with learning difficulties.</p>
    </div>

    <div class="photo" role="img" aria-label="Photo of a young student resting his head on a desk beside a notebook and pencil, looking tired"></div>
  </section>

</main>
</body>
</html>
```